New Business Card

We need to refresh our business cards. We designed these ourselves and we have no graphic design experience. We would like to find a new business card design that is professional and unique. We are an auto finance company. Feel free to play with the logo, but we would like to keep the eye very present on the card. Our corporate colors are green, grey, and white.
Green - RGB - 168,215,27; HEX - #AADD22
Grey - RGB - 196,196,196; HEX - #C4C4C4
Updates
Need to upload the vector file to finalize the project. The last logo was for a jpeg that didn't stretch well.
Industry/Entity Type
Financial Service
Contact Information for Business Card
Honestly don't know...I need your help!

```html
<!DOCTYPE html>
<html lang="en">
<head>
<meta charset="utf-8">
<title>Farview Capital – Business Card</title>
<link href="https://fonts.googleapis.com/css2?family=Roboto:wght@400;500;700&display=swap" rel="stylesheet">
<style>
  :root {
    --stage: #3a332f;
    --card: #1c1f22;
    --green: #aadd22;
    --grey: #c4c4c4;
    --white: #f2f2f2;
  }
  * { margin: 0; padding: 0; box-sizing: border-box; }
  html, body { width: 1200px; height: 769px; overflow: hidden; }
  body {
    background: var(--stage);
    font-family: "Roboto", Arial, sans-serif;
    position: relative;
  }
  .card {
    position: absolute;
    top: 230px;
    width: 525px;
    height: 300px;
    background: var(--card);
    border-radius: 3px;
    box-shadow: 0 10px 28px rgba(0,0,0,.45);
  }
  .card--front { left: 50px; }
  .card--back { left: 625px; }

  .brand {
    display: flex;
    align-items: center;
    gap: 12px;
    color: var(--green);
    font-weight: 500;
  }
  .brand__dot {
    width: 34px; height: 34px;
    border-radius: 50%;
    background: var(--green);
  }
  .card--front .brand {
    position: absolute;
    left: 0; right: 0; top: 112px;
    justify-content: center;
    font-size: 36px;
  }
  .card--front .brand__dot { width: 42px; height: 42px; }
  .front__web {
    position: absolute;
    left: 0; right: 0; top: 190px;
    text-align: center;
    color: var(--grey);
    font-size: 14px;
    letter-spacing: .5px;
  }

  .card--back .brand {
    position: absolute;
    right: 34px; top: 48px;
    font-size: 28px;
  }
  .holder { position: absolute; left: 34px; top: 40px; }
  .holder__name {
    color: var(--green);
    font-weight: 700;
    font-size: 17px;
    letter-spacing: .3px;
  }
  .holder__title {
    color: var(--grey);
    font-size: 13px;
    margin-top: 2px;
  }
  .contact { list-style: none; margin-top: 12px; }
  .contact li {
    display: flex;
    align-items: center;
    gap: 9px;
    color: var(--white);
    font-size: 13px;
    line-height: 19px;
  }
  .contact svg { width: 11px; height: 11px; fill: var(--green); flex: none; }
  .divider {
    position: absolute;
    left: 34px; right: 34px; top: 170px;
    height: 1px;
    background: var(--green);
  }
  .address {
    position: absolute;
    right: 34px; top: 196px;
    text-align: right;
    color: var(--white);
    font-size: 14px;
    line-height: 20px;
    font-style: normal;
  }
</style>
</head>
<body>
  <section class="card card--front" aria-label="Card front">
    <div class="brand"><span class="brand__dot"></span>Farview Capital</div>
    <p class="front__web">www.farviewcapital.com</p>
  </section>

  <section class="card card--back" aria-label="Card back">
    <div class="holder">
      <p class="holder__name">DANIEL REYES</p>
      <p class="holder__title">CEO/FOUNDER</p>
      <ul class="contact">
        <li><svg viewBox="0 0 12 12"><path d="M2.5 1l2 2-1 1.5c.7 1.5 1.8 2.6 3.3 3.3L8.3 6.8l2 2-1.3 2C5 10.5 1.5 7 1 3z"/></svg>555 210 4471</li>
        <li><svg viewBox="0 0 12 12"><path d="M3.5 0h5a1 1 0 0 1 1 1v10a1 1 0 0 1-1 1h-5a1 1 0 0 1-1-1V1a1 1 0 0 1 1-1zm.5 1.5v7.5h4V1.5z"/></svg>555 318 2906</li>
        <li><svg viewBox="0 0 12 12"><path d="M3 0h6v3H3zM1 4h10v6H9v2H3v-2H1zm3 4v3h4V8z"/></svg>555 742 6153</li>
        <li><svg viewBox="0 0 12 12"><path d="M0 2h12v8H0zm1 1v.4L6 6.6l5-3.2V3z"/></svg>hello@farviewcapital.com</li>
      </ul>
    </div>
    <div class="brand"><span class="brand__dot"></span>Farview Capital</div>
    <div class="divider"></div>
    <address class="address">
      1420 Juniper Street<br>
      Fairbanks, Alaska 99701<br>
      www.farviewcapital.com
    </address>
  </section>
</body>
</html>
```